New Branding Logo and Stationery Design Project

We are looking for a Stationary design for a company called "Peak Rebuilders". We are a Personal Training business that helps people of diverse ages, fitness levels and goals achieve what they aspire to. We are excellent at what we do and have a high rate of results. We are highly compassionate and love helping people. We want this to show in our logo. The logo must be able to be used on websites but also allow for large printing in the future also.

On the Business Card
Front we need the logo, and underneath this the words "Your health and fitness specialists".
On the back of the card we need:
Name (this will be different on the 2 peoples cards)
Health and fitness specialist
mobile: 04XX-XXX-XXX (we will give to the winner to add)
website: www.peakrebuilders.com.au
email: info@peakrebuilders.com.au
Down the bottom of the card we need a section that says something like:
"Your next appointment date is / / time : "

On the letterhead we will need:
Logo
Peak Rebuilders Pty Ltd
Address
Phone number
Email
Website

Target Market(s)

Anyone, any age who needs help with health and fitness

Industry/Entity Type

Printing

Requirements
Must have
• Templates for business cards here:
https://www.inkmarlow.com.au/businesscards_diy.php
Should not have
• Should not be Racist, Sexist, Ageist

```html
<!DOCTYPE html>
<html lang="en">
<head>
<meta charset="utf-8">
<title>Peak Rebuilders – Logo and Stationery</title>
<link rel="stylesheet" href="https://fonts.googleapis.com/css2?family=Andika&family=Tinos&display=swap">
<style>
  :root {
    --ink: #111111;
    --paper: #ffffff;
    --brand-red: #e8262b;
    --card-black: #0d0d0d;
    --peach: #fbe2d6;
    --label-font: "Tinos", "Times New Roman", serif;
    --text-font: "Andika", "Trebuchet MS", sans-serif;
  }
  * { box-sizing: border-box; margin: 0; padding: 0; }
  html, body { width: 1200px; height: 849px; overflow: hidden; background: var(--paper); }
  .sheet {
    position: relative;
    width: 1200px;
    height: 849px;
    border: 1px solid var(--ink);
    background: var(--paper);
    color: var(--ink);
  }
  .section-label {
    position: absolute;
    font-family: var(--label-font);
    font-size: 14px;
    text-align: center;
    line-height: 1.3;
  }
  .wordmark {
    position: absolute;
    display: flex;
    align-items: center;
    gap: 10px;
    font-family: var(--text-font);
    color: var(--ink);
    white-space: nowrap;
    line-height: 1;
  }
  .wordmark .mark-square {
    display: inline-block;
    background: var(--brand-red);
  }
  .wordmark--main { left: 170px; top: 92px; font-size: 38px; }
  .wordmark--main .mark-square { width: 20px; height: 20px; }
  .wordmark--alt { left: 188px; top: 222px; font-size: 30px; }
  .wordmark--alt .mark-square { width: 16px; height: 16px; }

  .card {
    position: absolute;
    left: 146px;
    width: 311px;
    height: 187px;
    border: 1px solid var(--ink);
    overflow: hidden;
  }
  .card--front { top: 410px; }
  .card--back { top: 618px; border: none; }
  .card--front .wordmark { left: 52px; top: 62px; font-size: 28px; gap: 8px; }
  .card--front .wordmark .mark-square { width: 14px; height: 14px; }
  .tagline {
    position: absolute;
    font-family: var(--text-font);
    font-size: 12px;
    white-space: nowrap;
  }
  .card--front .tagline { left: 0; width: 100%; top: 110px; text-align: center; }
  .card-back-art { display: block; width: 311px; height: 187px; }
  .card-back-art text { font-family: var(--text-font); }
  .card-back-art .contact-lines text { font-size: 8.5px; }
  .card-back-art .appointment text { font-size: 9.5px; }

  .letterhead {
    position: absolute;
    left: 566px;
    top: 37px;
    width: 549px;
    height: 775px;
    border: 2px solid var(--ink);
    overflow: hidden;
  }
  .letterhead-band {
    position: absolute;
    right: 0;
    top: 0;
    width: 180px;
    height: 130px;
    background: var(--peach);
  }
  .letterhead .wordmark { left: 30px; top: 48px; font-size: 30px; gap: 8px; }
  .letterhead .wordmark .mark-square { width: 14px; height: 14px; }
  .letterhead .tagline { left: 38px; top: 88px; font-size: 12px; }
  .letterhead-address {
    position: absolute;
    right: 35px;
    top: 28px;
    font-family: var(--text-font);
    font-size: 12.5px;
    line-height: 15.3px;
    text-align: right;
    font-style: normal;
  }
</style>
</head>
<body>
<main class="sheet">

  <p class="section-label" style="left:222px; top:34px; width:100px;">Logo.</p>
  <div class="wordmark wordmark--main"><span class="mark-square"></span>Peak Rebuilders</div>

  <p class="section-label" style="left:30px; top:214px; width:145px;">Legs can be added to stick figure lifting weights</p>
  <div class="wordmark wordmark--alt"><span class="mark-square"></span>Peak Rebuilders</div>

  <p class="section-label" style="left:232px; top:364px; width:140px;">Business Card.</p>

  <p class="section-label" style="left:40px; top:494px; width:66px;">Front</p>
  <section class="card card--front">
    <div class="wordmark"><span class="mark-square"></span>Peak Rebuilders</div>
    <p class="tagline">Your health and fitness specialists</p>
  </section>

  <p class="section-label" style="left:40px; top:698px; width:66px;">Back</p>
  <section class="card card--back">
    <svg class="card-back-art" viewBox="0 0 311 187" xmlns="http://www.w3.org/2000/svg">
      <rect width="311" height="187" fill="var(--paper)"/>
      <polygon points="0,0 190,0 44,187 0,187" fill="var(--card-black)"/>
      <polygon points="190,0 240,0 94,187 44,187" fill="var(--brand-red)"/>
      <g class="contact-lines" transform="translate(12,150) rotate(-52)" fill="var(--paper)">
        <text x="0" y="0">Name Sample</text>
        <text x="0" y="10">Health and fitness specialist</text>
        <text x="0" y="20">mobile: 04XX-XXX-XXX</text>
        <text x="0" y="30">website: www.peakrebuilders.com.au</text>
        <text x="0" y="40">email: info@peakrebuilders.com.au</text>
      </g>
      <g class="appointment" fill="var(--ink)">
        <text transform="translate(130,183) rotate(-52)">Your next appointment is:</text>
        <text transform="translate(172,179) rotate(-52)">Date:</text>
        <text transform="translate(242,110) rotate(-52)">Time:</text>
      </g>
    </svg>
  </section>

  <p class="section-label" style="left:780px; top:12px; width:120px;">Letterhead.</p>
  <section class="letterhead">
    <div class="letterhead-band" aria-hidden="true"></div>
    <div class="wordmark"><span class="mark-square"></span>Peak Rebuilders</div>
    <p class="tagline">Your health and fitness specialists</p>
    <address class="letterhead-address">
      10 Sample St<br>
      Sampletown, XXX, 2000<br>
      Phone: 04XX-XXX-XXX<br>
      website: www.peakrebuilders.com.au<br>
      email: info@peakrebuilders.com.au
    </address>
  </section>

</main>
</body>
</html>
```